cover arrangement / layout for "The Lantern Shelf Habit"

I want a cover layout (one for e-book, one for paperback) that is professional enough to compete with the likes of the Rolf Whitcombe, Dorian Pelk, Everett Castlemoor and Hugo Varnel's of the world. I have the book title logo, font, and color pallette - but I want some ideas for the cover (front cover only) layout.

I'm attaching the logo (white on transparent background), as well as the "sample" cover I've been using in mockups. I'm not looking for revolutionary designs or new logos, but rather a "cover" (the whole thing) design and arrangement.

Here are the parameters for the cover designs:

• eBook: 1600 x 2560 pixels, 72 ppi, RGB colorspace

• Physical book: 8.5 x 5.5 inches, 300 ppi, CMYK colorspace

For the physical book, if the designers don't extend the artwork to go outside the entire book, no bleeds need to be added.

We'll need the following from the winning designer(s):

1. An editable source file of the cover design, with open layers (AI; PSD); and

2. The fonts used. My brand fonts are Zing Rust Base, and Overpass. Those should be used, however I'm also open to alternative ideas as an additional consideration.

```html
<!DOCTYPE html>
<html lang="en">
<head>
<meta charset="utf-8">
<title>The Lantern Shelf Habit — Front Cover</title>
<link href="https://fonts.googleapis.com/css2?family=Bebas+Neue&display=swap" rel="stylesheet">
<style>
  :root {
    --stage-grey: #e4e4e4;
    --cover-white: #ffffff;
    --title-navy: #0035a3;
    --accent-blue: #0b50ea;
    --author-blue: #1656f2;
  }
  * { box-sizing: border-box; margin: 0; padding: 0; }
  html, body {
    width: 1200px;
    height: 1200px;
    overflow: hidden;
    background: var(--stage-grey);
  }
  .canvas {
    position: relative;
    width: 1200px;
    height: 1200px;
    background: var(--stage-grey);
  }
  .cover {
    position: absolute;
    left: 330px;
    top: 169px;
    width: 540px;
    height: 862px;
    background: var(--cover-white);
    box-shadow: 0 10px 30px rgba(0, 0, 0, 0.12);
    font-family: "Bebas Neue", "Oswald", sans-serif;
    text-align: center;
  }
  .cover__subtitle {
    position: absolute;
    top: 124px;
    left: 0;
    width: 100%;
    color: var(--accent-blue);
    font-size: 40px;
    line-height: 48px;
    letter-spacing: 0.5px;
  }
  .cover__title {
    position: absolute;
    top: 292px;
    left: 0;
    width: 100%;
    color: var(--title-navy);
    line-height: 0.9;
  }
  .cover__title-line { display: block; }
  .cover__title-line--small { font-size: 72px; }
  .cover__title-line--large { font-size: 124px; }
  .cover__title-line--medium { font-size: 104px; }
  .cover__author {
    position: absolute;
    top: 706px;
    left: 0;
    width: 100%;
    color: var(--author-blue);
    font-size: 72px;
    line-height: 1;
    letter-spacing: 1px;
  }
</style>
</head>
<body>
  <main class="canvas">
    <section class="cover">
      <p class="cover__subtitle">How to Re-Engage &amp;<br>Reignite Your Workforce</p>
      <h1 class="cover__title">
        <span class="cover__title-line cover__title-line--small">The</span>
        <span class="cover__title-line cover__title-line--large">Lantern</span>
        <span class="cover__title-line cover__title-line--medium">Shelf Habit</span>
      </h1>
      <p class="cover__author">Corwin Aldenby Jr</p>
    </section>
  </main>
</body>
</html>
```